Business Card Revision

Need to redesign my business cards for a new professional look. We are a courier company. You can go to www.qvroutefast.com to see what we do. The trucks have an old company name (Nimble) on them but that is the company we are just now
changing the name.

Target Market(s)

Potential clients. We service the automotive, plumbing, printing, air freight industries as well as many others.

Industry/Entity Type

Business

Contact Information for Business Card

QVrushline
20583 Palmer Fenwick Parkway
Cincinnati, Oh 45317

Howard T. Lassiter
President

howie@qvroutefast.com

Main: (513) 555-0147

```html
<!DOCTYPE html>
<html lang="en">
<head>
<meta charset="utf-8">
<title>QVrushline Business Card</title>
<link href="https://fonts.googleapis.com/css2?family=Ubuntu:wght@400;500;700&display=swap" rel="stylesheet">
<style>
  :root {
    --page-bg: #d6d0c8;
    --card-bg: #eef2f3;
    --brand-blue: #1f5fa8;
    --brand-blue-soft: #3a78b8;
    --brand-green: #2a8a3a;
    --brand-green-dark: #237a32;
    --text-blue: #2b5f96;
  }
  html, body {
    margin: 0;
    padding: 0;
    width: 1200px;
    height: 970px;
    overflow: hidden;
    background: var(--page-bg);
    font-family: "Ubuntu", sans-serif;
  }
  .business-card {
    position: absolute;
    left: 100px;
    top: 201px;
    width: 1000px;
    height: 568px;
    background: var(--card-bg);
    overflow: hidden;
    box-shadow: 0 10px 30px rgba(0,0,0,0.18);
  }
  .card-swooshes {
    position: absolute;
    inset: 0;
    width: 100%;
    height: 100%;
  }
  .brand-name {
    position: absolute;
    left: 725px;
    top: 182px;
    transform: translate(-50%, -50%);
    margin: 0;
    font-weight: 700;
    font-size: 78px;
    color: var(--brand-blue);
    letter-spacing: -1px;
    white-space: nowrap;
  }
  .contact-block {
    position: absolute;
    left: 53px;
    top: 222px;
    color: var(--text-blue);
  }
  .person-name {
    margin: 0;
    font-weight: 500;
    font-size: 35px;
    line-height: 40px;
    color: var(--brand-blue);
  }
  .person-title {
    margin: 0;
    font-size: 27px;
    line-height: 32px;
    color: var(--brand-green);
  }
  .address {
    margin: 22px 0 0;
    font-style: normal;
    font-size: 27px;
    line-height: 28px;
  }
  .contact-line {
    display: flex;
    align-items: center;
    gap: 10px;
    font-size: 27px;
    line-height: 38px;
    margin: 0;
  }
  .contact-line:first-of-type { margin-top: 20px; }
  .contact-icon {
    width: 30px;
    height: 26px;
    flex: none;
  }
  .website {
    margin: 4px 0 0;
    font-size: 26px;
    line-height: 34px;
    color: var(--brand-green);
  }
</style>
</head>
<body>
  <div class="business-card">
    <svg class="card-swooshes" viewBox="0 0 1040 590" preserveAspectRatio="none" aria-hidden="true">
      <path d="M0,0 H1040 V6 C720,10 300,70 0,225 Z" fill="var(--brand-blue-soft)"/>
      <path d="M1040,235 C860,420 520,545 0,556 V590 H1040 Z" fill="var(--brand-green)"/>
      <rect x="0" y="556" width="1040" height="34" fill="var(--brand-green-dark)"/>
    </svg>

    <p class="brand-name">QVrushline</p>

    <div class="contact-block">
      <h1 class="person-name">Howard T. Lassiter</h1>
      <p class="person-title">President</p>
      <address class="address">
        20583 Palmer Fenwick Parkway<br>
        Cincinnati, Oh 45317
      </address>
      <p class="contact-line">
        <svg class="contact-icon" viewBox="0 0 30 26" aria-hidden="true">
          <rect width="30" height="26" rx="2" fill="var(--brand-green)"/>
          <path d="M7,10 Q15,4 23,10 L21,13 L18,11 L12,11 L9,13 Z" fill="#fff"/>
          <rect x="9" y="14" width="12" height="7" rx="1" fill="#fff"/>
        </svg>
        (513) 555-0147
      </p>
      <p class="contact-line">
        <svg class="contact-icon" viewBox="0 0 30 26" aria-hidden="true">
          <rect width="30" height="26" rx="2" fill="var(--brand-green)"/>
          <rect x="6" y="7" width="18" height="12" fill="none" stroke="#fff" stroke-width="2"/>
          <path d="M6,7 L15,14 L24,7" fill="none" stroke="#fff" stroke-width="2"/>
        </svg>
        howie@qvroutefast.com
      </p>
      <p class="website">www.qvroutefast.com</p>
    </div>
  </div>
</body>
</html>
```